Billboard design - consider what a billboard is

Design a billboard using my logo - Billboard is 6m x 3m
A Billboard is advertising for my company that is on a big sign.

Has to be clean and easy to read, and ideally highlights that we are Residential and Commercial builders.

Keep it clean and easy to read

The contact number for the board is

022 583 7092
www.harbourframeworks.co.nz
info@harbourframeworks.co.nz

Doesnt have to have all contact details if it doesnt fit

Has to catch peoples attention to contact us if they need a builder

Can you please change the sign to be all white writing, with black background ?
Updates

Please consider what a billboard is...

The design needs to be suitable for a billboard..

Target Market(s)

people driving past

Industry/Entity Type

Construction

Logo Text

Wellington Builder, website email address, contact number

Colors
0054AA
0677BA
7BADD7
CADEEF
E8F1F8

Requirements
Must have
• Easy to read
Nice to have
• easy to read, can clearly see contact details

```html
<!DOCTYPE html>
<html lang="en">
<head>
<meta charset="UTF-8">
<title>Harbour Frameworks Billboard</title>
<link href="https://fonts.googleapis.com/css2?family=Poppins:wght@500;600&display=swap" rel="stylesheet">
<style>
  :root {
    --night: #000000;
    --brand-blue: #5a8ac6;
    --slate: #666666;
    --white: #ffffff;
  }
  * { margin: 0; padding: 0; box-sizing: border-box; }
  html, body { width: 1200px; height: 600px; overflow: hidden; background: var(--night); }
  .billboard {
    position: relative;
    width: 1200px;
    height: 600px;
    background: var(--night);
    font-family: "Poppins", sans-serif;
    color: var(--white);
  }
  .brand {
    position: absolute;
    left: 0; right: 0;
    top: 190px;
    display: flex;
    align-items: center;
    justify-content: center;
    gap: 26px;
  }
  .brand-mark {
    width: 58px; height: 58px;
    background: var(--white);
  }
  .brand-name {
    font-size: 66px;
    font-weight: 600;
    color: var(--white);
    letter-spacing: -0.5px;
    line-height: 1;
  }
  .tagline {
    position: absolute;
    left: 0; right: 0;
    top: 300px;
    text-align: center;
    font-size: 30px;
    font-weight: 500;
    letter-spacing: 1.5px;
    color: var(--white);
    line-height: 1;
  }
  .contact-tab {
    position: absolute;
    left: 504px;
    top: 442px;
    width: 192px;
    height: 32px;
    background: var(--brand-blue);
    border-radius: 30px 30px 0 0;
    color: var(--white);
    font-size: 23px;
    font-weight: 600;
    text-align: center;
    line-height: 35px;
    letter-spacing: 0.3px;
  }
  .contact-band {
    position: absolute;
    left: 0; top: 472px;
    width: 1200px; height: 128px;
    background: var(--slate);
    display: flex;
    align-items: center;
    justify-content: center;
    gap: 24px;
    color: var(--white);
    font-size: 27.5px;
    font-weight: 500;
    padding-bottom: 8px;
  }
  .divider { width: 6px; height: 36px; display: block; }
</style>
</head>
<body>
  <main class="billboard">
    <div class="brand">
      <span class="brand-mark"></span>
      <span class="brand-name">Harbour Frameworks</span>
    </div>
    <p class="tagline">Residential &amp; Commercial Builders</p>

    <div class="contact-tab">Contact Us</div>

    <footer class="contact-band">
      <span class="contact-phone">022 583 7092</span>
      <svg class="divider" viewBox="0 0 6 36" aria-hidden="true"><polygon points="1,6 5,0 5,30 1,36" fill="#ffffff"/></svg>
      <span class="contact-web">www.harbourframeworks.co.nz</span>
      <svg class="divider" viewBox="0 0 6 36" aria-hidden="true"><polygon points="1,6 5,0 5,30 1,36" fill="#ffffff"/></svg>
      <span class="contact-email">info@harbourframeworks.co.nz</span>
    </footer>
  </main>
</body>
</html>
```